RW Soundworks Web Site Design

Need a basic site to show clients a little about what we do. We are a custom audio video company in the high-end residential market. Need a few basic but professional pages to show past projects and products we sell. No e-commerce. Should include my new logo from MarkHive.

Industry/Entity Type

Residential

Number of Pages Required

2 page

Font styles to use
Serif
Sans Serif

Colors
f78f20

Requirements
Must have
• Company Logo, Send feedback page
Nice to have
• I have no ideas about design, but I do know what I like and dislike when I see it.

```html
<!DOCTYPE html>
<html lang="en">
<head>
<meta charset="utf-8">
<title>RW Soundworks — Audio Video Control</title>
<link rel="stylesheet" href="https://fonts.googleapis.com/css2?family=Arimo:wght@400;700&family=Quicksand:wght@500;700&family=Roboto+Slab:wght@300;400&display=swap">
<style>
  :root {
    --orange: #f78f20;
    --black: #1c1c1c;
    --header-bg: #eef2fb;
    --services-bg: #bcc0bc;
    --projects-bg: #4a4a4a;
    --footer-bg: #3b3b3b;
    --white: #ffffff;
    --text-dark: #2b2b2b;
  }
  * { margin: 0; padding: 0; box-sizing: border-box; }
  html, body { width: 1016px; height: 1200px; overflow: hidden; }
  body { position: relative; font-family: "Arimo", Arial, sans-serif; background: var(--white); }

  .site-header { position: absolute; left: 0; top: 0; width: 1016px; height: 70px; background: var(--header-bg); }
  .main-nav { position: absolute; left: 0; top: 70px; width: 1016px; height: 30px; background: var(--black); }
  .brand { position: absolute; left: 110px; top: 0; width: 236px; height: 100px; background: var(--header-bg);
    display: flex; align-items: center; gap: 10px; padding-left: 8px; }
  .brand-mark { width: 56px; height: 56px; background: var(--orange); border-radius: 6px; flex: none; }
  .brand-name { font-family: "Quicksand", sans-serif; font-weight: 700; font-size: 22px; color: var(--text-dark); line-height: 1.05; }

  .schedule-btn { position: absolute; left: 512px; top: 31px; width: 222px; height: 28px; background: var(--black);
    border-radius: 2px; color: var(--orange); font-family: "Roboto Slab", serif; font-size: 15px;
    display: flex; align-items: center; justify-content: center; }
  .phone-icon { position: absolute; left: 755px; top: 30px; width: 26px; height: 26px; }
  .phone-label { position: absolute; left: 787px; top: 27px; font-size: 12px; color: var(--text-dark); }
  .phone-number { position: absolute; left: 787px; top: 41px; font-size: 18px; color: var(--text-dark); }

  .nav-list { position: absolute; top: 70px; left: 0; list-style: none; }
  .nav-list li { position: absolute; top: 0; height: 30px; line-height: 30px; font-size: 12px; color: var(--orange); white-space: nowrap; }
  .nav-list li.is-active { background: var(--orange); color: var(--black); width: 67px; text-align: center; }

  .hero { position: absolute; left: 0; top: 100px; width: 1016px; height: 317px;
    background: linear-gradient(135deg, #cfc4b4 0%, #9c8f7f 30%, #e8e4dc 55%, #8b7d6b 80%, #5a4f43 100%); }
  .hero-arrow { position: absolute; top: 156px; width: 30px; height: 28px; background: #2a2a2a; }
  .hero-arrow.prev { left: 6px; } .hero-arrow.next { left: 978px; }
  .hero-caption { position: absolute; left: 137px; top: 283px; width: 751px; height: 34px; background: rgba(60,60,60,.6);
    color: var(--white); font-family: "Quicksand", sans-serif; font-weight: 500; font-size: 18px;
    display: flex; align-items: center; justify-content: center; }

  .services { position: absolute; left: 0; top: 417px; width: 1016px; height: 323px; background: var(--services-bg); }
  .service { position: absolute; top: 30px; width: 180px; text-align: center; }
  .service-tile { width: 125px; height: 125px; margin: 26px auto 0; transform: rotate(45deg); border-radius: 14px; }
  .service-name { margin-top: 50px; font-family: "Roboto Slab", serif; font-weight: 300; font-size: 18px; line-height: 19px; color: var(--white); }

  .about { position: absolute; left: 0; top: 740px; width: 1016px; height: 193px; background: var(--orange); text-align: center; color: var(--white); }
  .section-title { font-family: "Quicksand", sans-serif; font-weight: 700; font-size: 23px; }
  .about .section-title { margin-top: 26px; }
  .title-rule { margin: 6px auto 0; border-top: 1px dashed; }
  .about .title-rule { width: 356px; border-color: #2a5a9a; }
  .about-text { width: 780px; margin: 13px auto 0; font-family: "Roboto Slab", serif; font-weight: 300; font-size: 11.5px; line-height: 16.7px; }
  .read-more { display: inline-block; margin-top: 11px; font-family: "Roboto Slab", serif; font-size: 11.5px; color: var(--white); text-decoration: underline; }

  .projects { position: absolute; left: 0; top: 933px; width: 1016px; height: 231px; background: var(--projects-bg); text-align: center; color: var(--white); }
  .projects .section-title { margin-top: 24px; }
  .projects .title-rule { width: 238px; border-color: #8a8a8a; }
  .project-card { position: absolute; top: 79px; width: 139px; height: 110px; border: 1px solid var(--orange); border-radius: 8px; padding: 4px; }
  .project-photo { width: 100%; height: 100%; border-radius: 7px; border: 1px solid #ddd; }
  .project-overlay { position: absolute; inset: 4px; border-radius: 7px; background: rgba(255,255,255,.7);
    display: flex; align-items: center; justify-content: center; font-family: "Roboto Slab", serif; font-size: 13px; line-height: 17px; color: var(--text-dark); }
  .carousel-arrow { position: absolute; top: 120px; width: 22px; height: 38px; }

  .site-footer { position: absolute; left: 0; top: 1164px; width: 1016px; height: 36px; background: var(--footer-bg); color: #e6e6e6; font-size: 10.5px; }
  .copyright { position: absolute; left: 138px; top: 14px; }
  .accept-label { position: absolute; left: 650px; top: 12px; }
  .payment-cards { position: absolute; left: 705px; top: 5px; display: flex; gap: 5px; }
  .payment-card { width: 42px; height: 26px; border-radius: 3px; }
</style>
</head>
<body>
  <header class="site-header">
    <div class="schedule-btn">Schedule Your Work Service</div>
    <svg class="phone-icon" viewBox="0 0 26 26" aria-hidden="true">
      <circle cx="13" cy="13" r="11.5" fill="none" stroke="#f78f20" stroke-width="1.6"/>
      <path d="M9 7c-1 1-1.5 3 0 6s4 5.5 6.5 6.5c1.5.5 2.5-.5 3-1.5l-2-2-1.5 1c-1.5-.8-3-2.5-3.7-4l1-1.5-2-2.5z" fill="#f78f20"/>
    </svg>
    <div class="phone-label">Call Us Today</div>
    <div class="phone-number">555-214-7730</div>
  </header>

  <nav class="main-nav"></nav>
  <div class="brand">
    <span class="brand-mark"></span>
    <span class="brand-name">RW<br>Soundworks</span>
  </div>
  <ul class="nav-list">
    <li class="is-active" style="left:346px">HOME</li>
    <li style="left:433px">ABOUT US</li>
    <li style="left:507px">PRODUCT &amp; SERVICES</li>
    <li style="left:648px">PAST PROJECT</li>
    <li style="left:747px">FEEDBACK</li>
    <li style="left:824px">CONTACT US</li>
  </ul>

  <section class="hero" role="img" aria-label="Photo of a bright living room with white sofas, stone walls and a wall-mounted TV">
    <svg class="hero-arrow prev" viewBox="0 0 30 28" aria-hidden="true"><path d="M17 9l-5 5 5 5" stroke="#fff" stroke-width="2.5" fill="none"/></svg>
    <svg class="hero-arrow next" viewBox="0 0 30 28" aria-hidden="true"><path d="M13 9l5 5-5 5" stroke="#fff" stroke-width="2.5" fill="none"/></svg>
    <div class="hero-caption">We are a custom audio video company in the high-end residential market</div>
  </section>

  <section class="services">
    <div class="service" style="left:118px">
      <div class="service-tile" role="img" aria-label="Security camera photo" style="background:linear-gradient(135deg,#2a2a2a,#1a1a1a)"></div>
      <p class="service-name">CCTV<br>Surveillance Systems</p>
    </div>
    <div class="service" style="left:328px">
      <div class="service-tile" role="img" aria-label="Video conference room photo" style="background:linear-gradient(135deg,#8a96a8,#6b5a44)"></div>
      <p class="service-name">Teleconferencing<br>Solutions</p>
    </div>
    <div class="service" style="left:524px">
      <div class="service-tile" role="img" aria-label="Automated home interior photo" style="background:linear-gradient(135deg,#c8c8c2,#6f7670)"></div>
      <p class="service-name">Automation<br>Systems</p>
    </div>
    <div class="service" style="left:718px">
      <div class="service-tile" role="img" aria-label="Fingerprint access panel photo" style="background:linear-gradient(135deg,#111,#2b2b35)"></div>
      <p class="service-name">Access<br>Control Solutions</p>
    </div>
  </section>

  <section class="about">
    <h2 class="section-title">About RW Soundworks</h2>
    <div class="title-rule"></div>
    <p class="about-text">Lorem ipsum dolor sit amet, consectetuer adipiscing elit, sed diam nmmy nibh euismod tincidunt ut laoreet dolore magna aliquam erat volutpat. Ut wisi enim ad minim veniam, quis nostrud exerci tation ullamcorper suscipit lobortis nisl ut aliquip modo consequat. Duis autem vel eum iriure dolor in hendrerit in vulputate velit esse mtie consequat, vel illum dolore eu feugiat nulla facilisis at vero eros et accumsan et iust odio dignissim qui blandit praesent luptatum zzril delenit augue duis dolore te feugait nulla facilisi.</p>
    <a class="read-more">Read More</a>
  </section>

  <section class="projects">
    <h2 class="section-title">Past Projects</h2>
    <div class="title-rule"></div>
    <svg class="carousel-arrow" style="left:80px" viewBox="0 0 22 38" aria-hidden="true"><path d="M20 2L3 19l17 17" stroke="#ddd" stroke-width="1.8" fill="none"/></svg>
    <div class="project-card" style="left:121px">
      <div class="project-photo" role="img" aria-label="Home theater room photo" style="background:linear-gradient(135deg,#d8cfc2,#9e8e78)"></div>
      <div class="project-overlay">Lorem ipsum<br>dolor sit amet,<br>consectetuer<br>adipiscing.</div>
    </div>
    <div class="project-card" style="left:280px">
      <div class="project-photo" role="img" aria-label="Vehicle cabin with overhead screen photo" style="background:linear-gradient(135deg,#5a7fb0,#c9c0ae)"></div>
    </div>
    <div class="project-card" style="left:440px">
      <div class="project-photo" role="img" aria-label="TV mounted above a stone fireplace photo" style="background:linear-gradient(135deg,#4a3a30,#8a7060)"></div>
    </div>
    <div class="project-card" style="left:599px">
      <div class="project-photo" role="img" aria-label="Outdoor speaker on wooden post photo" style="background:linear-gradient(135deg,#8a4a20,#d08848)"></div>
    </div>
    <div class="project-card" style="left:759px">
      <div class="project-photo" role="img" aria-label="Living room TV installation photo" style="background:linear-gradient(135deg,#d6a84a,#b89a70)"></div>
    </div>
    <svg class="carousel-arrow" style="left:908px" viewBox="0 0 22 38" aria-hidden="true"><path d="M2 2l17 17L2 36" stroke="#ddd" stroke-width="1.8" fill="none"/></svg>
  </section>

  <footer class="site-footer">
    <span class="copyright">Copyright ©2015 RWSoundworks.&nbsp; All Rights Reserved.</span>
    <span class="accept-label">We Accept</span>
    <div class="payment-cards">
      <span class="payment-card" style="background:#1f5fb0"></span>
      <span class="payment-card" style="background:#f2f2f2"></span>
      <span class="payment-card" style="background:#e8e8ee"></span>
      <span class="payment-card" style="background:#3a8fd0"></span>
      <span class="payment-card" style="background:#d0302a"></span>
    </div>
  </footer>
</body>
</html>
```